Investment Management Firm Power point template

Kestrel Holdings is a real estate investment firm focused on buying commercial office and residential property in the UK. We produce powerpoint presentations for our Board of Directors, Investment Committee and also to external investors.

We are looking for a powerpoint design template which we can use for future presentations which provide a professional look and feel.

Our current website: http://www.kestrelholdings-example.co.uk/

Target Market(s)

Institution Investors, Board of Directors, Professionals

Industry/Entity Type

Real Estate

Requirements
Must have
• Leverage off the current logo and colour scheme. However, does not have to purely rely on this colour scheme.
• - Title page
• - Content Page
• - Slide where graphs can be incorporated
• - Slide where photos can be incorporated
• - Slide of UK Map which can show where the property portfolio is currently located
• - Other slides incorporating smart art or other designs that can be used for future presentations
Nice to have
• An example of graphics that we would love to have in the powerpoint pack which we can easily edit has been attached

```html
<!DOCTYPE html>
<html lang="en">
<head>
<meta charset="utf-8">
<title>About Us</title>
<link rel="stylesheet" href="https://fonts.googleapis.com/css2?family=Titillium+Web:wght@600;700&family=Catamaran:wght@400&display=swap">
<style>
  :root {
    --brand: #1f5a7c;
    --brand-dark: #2a5a78;
    --text: #2e2e2e;
    --page: #ffffff;
    --footer: #333333;
    --pattern-a: #ececec;
    --pattern-b: #ffffff;
  }
  * { margin: 0; padding: 0; box-sizing: border-box; }
  html, body { width: 1200px; height: 900px; overflow: hidden; background: var(--page); }
  .slide {
    position: relative;
    width: 1200px;
    height: 900px;
    overflow: hidden;
    background: var(--page);
  }
  .backdrop {
    position: absolute;
    inset: 0 0 39px 0;
    background:
      radial-gradient(ellipse 620px 520px at 120px 150px, var(--pattern-a) 0%, rgba(236,236,236,0.45) 45%, rgba(255,255,255,0) 75%),
      linear-gradient(180deg, #f6f6f6 0%, var(--pattern-b) 85%);
  }
  .slide-title {
    position: absolute;
    top: 22px;
    left: 0;
    width: 100%;
    text-align: center;
    font-family: "Titillium Web", sans-serif;
    font-weight: 700;
    font-size: 42px;
    line-height: 58px;
    color: var(--brand);
  }
  .title-rule {
    position: absolute;
    top: 76px;
    left: 470px;
    width: 262px;
    height: 1.5px;
    background: var(--brand);
  }
  .topic-list { list-style: none; }
  .topic {
    position: absolute;
    left: 40px;
    width: 1100px;
  }
  .topic-marker {
    position: absolute;
    left: 0;
    top: 6px;
    width: 44px;
    height: 42px;
    background: var(--brand-dark);
  }
  .topic-body { margin-left: 71px; }
  .topic-heading {
    font-family: "Titillium Web", sans-serif;
    font-weight: 600;
    font-size: 29px;
    line-height: 36px;
    color: var(--brand-dark);
  }
  .topic-text {
    font-family: "Catamaran", sans-serif;
    font-weight: 400;
    font-size: 22.5px;
    line-height: 36px;
    color: var(--text);
    width: 1010px;
  }
  .footer-band {
    position: absolute;
    left: 0;
    bottom: 0;
    width: 100%;
    height: 39px;
    background: var(--footer);
  }
</style>
</head>
<body>
<main class="slide">
  <div class="backdrop" role="img" aria-label="Soft grey halftone dot pattern fading across the page"></div>

  <h1 class="slide-title">About Us</h1>
  <div class="title-rule"></div>

  <ul class="topic-list">
    <li class="topic" style="top:150px">
      <span class="topic-marker"></span>
      <div class="topic-body">
        <h2 class="topic-heading">Subtitle Here</h2>
        <p class="topic-text">Lorem ipsum dolor sit ipsum Lorem ipsum dolor sit ipsum Lorem ipsum dolor sit ipsum Lorem ipsum dolor sit ipsum Lorem ipsum dolor sit ipsum Lorem ipsum dolor sit ipsum</p>
      </div>
    </li>
    <li class="topic" style="top:294px">
      <span class="topic-marker"></span>
      <div class="topic-body">
        <h2 class="topic-heading">Subtitle Here</h2>
        <p class="topic-text">Lorem ipsum dolor sit ipsum Lorem ipsum dolor sit ipsum Lorem ipsum dolor sit ipsum Lorem ipsum dolor sit ipsum Lorem ipsum dolor sit ipsum Lorem ipsum dolor sit ipsum</p>
      </div>
    </li>
    <li class="topic" style="top:438px">
      <span class="topic-marker"></span>
      <div class="topic-body">
        <h2 class="topic-heading">Subtitle Here</h2>
        <p class="topic-text">Lorem ipsum dolor sit ipsum Lorem ipsum dolor sit ipsum Lorem ipsum dolor sit ipsum Lorem ipsum dolor sit ipsum Lorem ipsum dolor sit ipsum Lorem ipsum dolor sit ipsum</p>
      </div>
    </li>
    <li class="topic" style="top:582px">
      <span class="topic-marker"></span>
      <div class="topic-body">
        <h2 class="topic-heading">Subtitle Here</h2>
        <p class="topic-text">Lorem ipsum dolor sit ipsum Lorem ipsum dolor sit ipsum Lorem ipsum dolor sit ipsum Lorem ipsum dolor sit ipsum Lorem ipsum dolor sit ipsum Lorem ipsum dolor sit ipsum dolor sit ipsumsit ipsum Lorem ipsum dolor sit ipsum</p>
      </div>
    </li>
  </ul>

  <div class="footer-band"></div>
</main>
</body>
</html>
```